Pop punk gig poster design!

In need of an amazing poster design for a gig We are organising, the genre is pop punk, and will be an all ages gig. I need to it bold, random and capture the eye of any bypasses, and make people want to go to the gig just because the poster is awesome! The event will be called "A glimpse of neon" and will consist of three bands and an acoustic set to open. All the bands are full of energy and create an unreal ambiance during there shows, I would like to capture that in the poster. Open to anything spectacular, the sky is the limit.

• I need to have the name of the event "A Glimpse Of Neon"
Band names(in this order):
-Fold the Lantern
-Velvet Orchard
-Gemwick's Oar
-Lunetta Pribble

Date: Saturday 10th November 2012
Time: 5:15pm
Venue: The Quill, 47 Marrowfen street, West End, QLD 4101
Ticket price: $10+bf online
$15 at the door.
Free BBQ

```html
<!DOCTYPE html>
<html lang="en">
<head>
<meta charset="utf-8">
<title>A Glimpse Of Neon – Gig Poster</title>
<link rel="stylesheet" href="https://fonts.googleapis.com/css2?family=Londrina+Solid:wght@400;900&family=Fira+Sans+Extra+Condensed:wght@700;800&display=swap">
<style>
  :root {
    --neon-lime: #c6f53a;
    --lime-light: #d3ff55;
    --lime-deep: #8fbf12;
    --ink: #0d0d0a;
    --stripe-dark: #1a1f08;
    --title-glow: #5f8a0a;
    --pig-gold: #d9b23a;
    --pig-cream: #f2efe4;
  }
  * { margin: 0; padding: 0; box-sizing: border-box; }
  html, body { width: 848px; height: 1200px; overflow: hidden; background: #ffffff; }
  .poster {
    position: relative;
    width: 848px;
    height: 1200px;
    overflow: hidden;
    background: var(--neon-lime);
  }
  .border-pattern {
    position: absolute;
    inset: 0;
    background: linear-gradient(135deg, var(--stripe-dark) 0%, var(--lime-deep) 30%, var(--stripe-dark) 55%, var(--lime-deep) 80%, var(--stripe-dark) 100%);
  }
  .panel {
    position: absolute;
    left: 70px;
    top: 98px;
    width: 722px;
    height: 1054px;
    background: radial-gradient(ellipse at 50% 40%, var(--lime-light) 0%, var(--neon-lime) 70%, #b9ea2e 100%);
  }
  .display {
    font-family: "Londrina Solid", "Arial Narrow", sans-serif;
    font-variant: small-caps;
    color: var(--ink);
    line-height: 1;
    white-space: nowrap;
  }
  .event-title {
    position: absolute;
    left: 140px;
    top: 122px;
    width: 596px;
    text-align: center;
    font-weight: 900;
    font-size: 84px;
    letter-spacing: 1px;
    text-shadow: 3px 3px 0 var(--title-glow), -1px -1px 0 #eaffb0;
  }
  .event-date {
    position: absolute;
    left: 128px;
    top: 246px;
    width: 616px;
    text-align: center;
    font-weight: 400;
    font-size: 54px;
  }
  .event-time {
    position: absolute;
    right: 104px;
    top: 312px;
    font-weight: 400;
    font-size: 54px;
    font-variant: normal;
  }
  .lineup {
    position: absolute;
    right: 120px;
    top: 426px;
    list-style: none;
    text-align: right;
  }
  .lineup li {
    font-weight: 400;
    font-size: 68px;
    height: 90px;
  }
  .singer-silhouette {
    position: absolute;
    left: 72px;
    top: 314px;
    width: 186px;
    height: 628px;
    background: linear-gradient(180deg, #1b1b16 0%, var(--ink) 100%);
    border-radius: 80px 80px 24px 24px;
  }
  .chef-pig {
    position: absolute;
    left: 500px;
    top: 755px;
    width: 245px;
    height: 240px;
    border-radius: 50%;
    background: radial-gradient(circle at 45% 35%, var(--pig-cream) 0%, var(--pig-gold) 60%, #9c7a1e 100%);
  }
  .info {
    position: absolute;
    font-family: "Fira Sans Extra Condensed", "Arial Narrow", sans-serif;
    color: var(--ink);
    line-height: 1;
    white-space: nowrap;
    text-shadow: 2px 2px 0 var(--title-glow);
  }
  .free-bbq { left: 250px; top: 934px; font-weight: 700; font-size: 46px; }
  .venue { left: 130px; top: 1014px; width: 600px; text-align: center; font-weight: 800; font-size: 34px; letter-spacing: -0.8px; }
  .tickets { left: 134px; top: 1062px; font-weight: 800; font-size: 33px; letter-spacing: -0.6px; }
  .tickets .door { margin-left: 18px; }
</style>
</head>
<body>
  <main class="poster">
    <div class="border-pattern" role="img" aria-label="Black and neon-lime zebra stripe pattern forming the poster frame"></div>
    <div class="panel"></div>

    <h1 class="display event-title">A Glimpse Of Neon</h1>
    <p class="display event-date">Saturday 10th November 2012</p>
    <p class="display event-time">5:15pm</p>

    <div class="singer-silhouette" role="img" aria-label="Black silhouette of a spiky-haired punk singer holding a microphone"></div>

    <ul class="lineup">
      <li class="display">Fold the Lantern</li>
      <li class="display">Velvet Orchard</li>
      <li class="display">Gemwick's Oar</li>
      <li class="display">Lunetta Pribble</li>
    </ul>

    <div class="chef-pig" role="img" aria-label="Cartoon golden pig wearing a white chef's hat, for the barbecue"></div>

    <p class="info free-bbq">Free BBQ</p>
    <p class="info venue">The Quill, 47 Marrowfen street, West End, QLD 4101</p>
    <p class="info tickets">Ticket price: $10+bf online <span class="door">$15 at the door.</span></p>
  </main>
</body>
</html>
```